Cobalt Ridge Physician Advising

I need a one-page advertisement that I can email to potential clients.

The target audience is hospital administrators.

I want it to include the logo, as attached. We specialize in Payer Denial Management. We are certified physician advisors with over 80 years combined clinical medicine experience. We have expertise in Utilization Management, Clinical Documentation Integrity, Peer to Peer Appeals and Letter Appeal Management. We win over 60% of our Peer to Peer Appeals with Medicare Advantage plans and over 50% of our first level letters.

We make sure hospitals get paid for the care they provide, I really want to emphasize that we are very effective at overturning insurance payment denials. We also provider other physician advising services. We keep our company small so that our rates are very affordable. Include that references are available.

We need to include: Contact us today, we can improve your revenue. Please 518-627-4083
or email (I will provide this later).

I want it to look professional but not bland, with maybe AI created images of a small group of physicians (mature, white coats, stethoscopes) looking at a spreadsheet on a laptop. a picture of a stack of money setting on a table, with a hand removing part of the money from the stack.

Companies like ours include Travenko, Q7, Halverick, Med-Lumora, and VantecoMD. Their websites may provide ideas.

Target Market(s)

Healthcare administrators who need to improve their hospital revenue

Industry/Entity Type

Healthcare consulting

Font styles to use
Sans Serif

Colors
0094D4
00A9DD
6FCCEA
C7EBF8
E9F6FB
00AB8E
00BBA5
67D7C9
C6EFE9
E9F9F6
FFC000
F8CF3A
FAE287
FDF2CF
FEFAEE
EE7325
F08F49
F5BC92
FAE3D3
FDF4ED
E54698
E96AAD
F1A4CE
F9D9EA
FCEFF6
6B429C
8869AF
B7A5CE
E3DAEB
F3F0F8

Requirements
Must have
• Must include that we are very successful here to appear in Peer to Peer appeals and Letter appeals
Nice to have
• Very easy to read, big bold fonts
Should not have
• I’m very afraid of having a lot of dark blues, combined with dark gold, because it may look like the colors of a health system in my area

```html
<!DOCTYPE html>
<html lang="en">
<head>
<meta charset="utf-8">
<title>Cobalt Ridge Physician Advising – Payer Denial Management</title>
<link rel="stylesheet" href="https://fonts.googleapis.com/css2?family=Plus+Jakarta+Sans:wght@400;500;700;800&display=swap">
<style>
  :root {
    --blue: #0094D4;
    --blue-light: #00A9DD;
    --green: #00AB8E;
    --white: #FFFFFF;
    --pale: #E9F6FB;
    --photo-top: #cfd8df;
    --photo-bottom: #7d8c99;
    --desk-light: #b8a48a;
    --desk-dark: #55585e;
  }
  * { margin: 0; padding: 0; box-sizing: border-box; }
  html, body { width: 848px; height: 1200px; overflow: hidden; background: var(--blue); }
  body { font-family: "Plus Jakarta Sans", sans-serif; color: var(--white); }
  .flyer { position: relative; width: 848px; height: 1200px; background: var(--blue); overflow: hidden; }
  .backdrop { position: absolute; inset: 0; }
  .brand { position: absolute; left: 0; width: 412px; top: 362px; text-align: center; }
  .brand-dot { width: 64px; height: 64px; border-radius: 50%; background: var(--green); margin: 0 auto 20px; }
  .brand-name { font-weight: 700; font-size: 36px; line-height: 38px; letter-spacing: -0.8px; }
  .brand-sub { font-weight: 700; font-size: 18px; line-height: 26px; letter-spacing: 0.6px; }
  .badge { position: absolute; left: 548px; top: 405px; width: 154px; height: 154px; border-radius: 50%; background: var(--green); display: flex; align-items: center; justify-content: center; }
  .badge::before { content: ""; position: absolute; inset: 12px; border: 2px dashed var(--white); border-radius: 50%; }
  .badge-text { font-weight: 800; font-size: 16px; line-height: 18px; text-align: center; margin-top: -28px; }
  .headline { position: absolute; left: 56px; top: 552px; font-weight: 800; font-size: 45px; line-height: 55px; letter-spacing: -0.3px; }
  .intro { position: absolute; left: 56px; top: 736px; font-weight: 400; font-size: 21.5px; line-height: 26px; width: 390px; }
  .value-note { position: absolute; left: 56px; top: 824px; font-weight: 700; font-size: 15px; line-height: 20px; color: var(--pale); }
  .availability { position: absolute; left: 56px; top: 866px; font-weight: 800; font-size: 23px; line-height: 32px; }
  .cta { position: absolute; left: 0; top: 959px; width: 316px; height: 56px; background: var(--green); border-radius: 0 28px 28px 0; padding: 8px 0 0 56px; }
  .cta-title { font-weight: 800; font-size: 21px; line-height: 24px; }
  .cta-sub { font-weight: 700; font-size: 13px; line-height: 16px; }
  .cta-arrow { position: absolute; right: 14px; top: 11px; width: 34px; height: 34px; }
  .contact { position: absolute; left: 56px; display: flex; align-items: center; gap: 18px; font-weight: 800; font-size: 23px; }
  .contact-icon { width: 34px; height: 34px; border-radius: 50%; background: var(--white); display: flex; align-items: center; justify-content: center; }
  .contact-phone { top: 1050px; }
  .contact-web { top: 1102px; }
  .results { position: absolute; left: 481px; top: 572px; list-style: none; font-weight: 700; font-size: 14px; line-height: 20px; }
  .results strong { font-weight: 800; font-size: 16px; }
  .services { position: absolute; left: 481px; top: 636px; }
  .services-title { font-weight: 800; font-size: 26px; line-height: 36px; margin-bottom: 20px; }
  .service-list { list-style: none; }
  .service-item { display: flex; align-items: center; gap: 16px; font-weight: 400; font-size: 18.5px; height: 44.7px; }
  .tick { width: 24px; height: 24px; flex: none; }
  .desk-photo { position: absolute; left: 483px; top: 906px; }
</style>
</head>
<body>
<main class="flyer">
  <svg class="backdrop" width="848" height="1200" viewBox="0 0 848 1200">
    <defs>
      <linearGradient id="teamTone" x1="0" y1="0" x2="0" y2="1">
        <stop offset="0" stop-color="var(--photo-top)"/>
        <stop offset="1" stop-color="var(--photo-bottom)"/>
      </linearGradient>
    </defs>
    <path class="accent-band" fill="var(--blue-light)" d="M0 0 L100 0 C170 230 330 420 520 462 L515 470 C300 440 120 300 0 135 Z"/>
    <path class="team-photo" fill="url(#teamTone)" role="img" aria-label="Photo: group of mature physicians in white coats with stethoscopes reviewing a spreadsheet on a laptop" d="M100 0 C170 230 330 420 520 462 C640 485 770 470 848 505 L848 0 Z"/>
  </svg>

  <div class="brand">
    <div class="brand-dot"></div>
    <div class="brand-name">COBALT RIDGE</div>
    <div class="brand-sub">PHYSICIAN ADVISING</div>
  </div>

  <div class="badge"><div class="badge-text">80 YEARS<br>EXPERIENCE</div></div>

  <h1 class="headline">We specialize<br>in Payer Denial<br>Management</h1>
  <p class="intro">We are certified physician advisors with over 80 years combined clinical medicine experience.</p>
  <p class="value-note">Affordable rates · References available</p>
  <p class="availability">We Are<br>Available 24/7</p>

  <div class="cta">
    <div class="cta-title">Contact us today</div>
    <div class="cta-sub">We can improve your revenue</div>
    <svg class="cta-arrow" viewBox="0 0 34 34"><circle cx="17" cy="17" r="15.5" fill="none" stroke="var(--white)" stroke-width="2.5"/><path d="M14 10 L21 17 L14 24" fill="none" stroke="var(--white)" stroke-width="2.8" stroke-linecap="round" stroke-linejoin="round"/></svg>
  </div>

  <div class="contact contact-phone">
    <span class="contact-icon"><svg width="18" height="18" viewBox="0 0 24 24"><path d="M6.6 10.8a15.1 15.1 0 0 0 6.6 6.6l2.2-2.2a1 1 0 0 1 1-.25 11.4 11.4 0 0 0 3.6.57 1 1 0 0 1 1 1V20a1 1 0 0 1-1 1A17 17 0 0 1 3 4a1 1 0 0 1 1-1h3.5a1 1 0 0 1 1 1c0 1.25.2 2.45.57 3.57a1 1 0 0 1-.25 1z" fill="none" stroke="var(--green)" stroke-width="1.5"/></svg></span>
    <span>518-627-4083</span>
  </div>
  <div class="contact contact-web">
    <span class="contact-icon"><svg width="18" height="18" viewBox="0 0 24 24" fill="none" stroke="var(--green)" stroke-width="1.5"><circle cx="12" cy="12" r="9"/><ellipse cx="12" cy="12" rx="4" ry="9"/><path d="M3 12h18M5 7h14M5 17h14"/></svg></span>
    <span>www.website.com</span>
  </div>

  <ul class="results">
    <li><strong>60%+</strong> of Peer to Peer appeals won (MA plans)</li>
    <li><strong>50%+</strong> of first-level letter appeals won</li>
  </ul>

  <section class="services">
    <h2 class="services-title">Our Services:</h2>
    <ul class="service-list">
      <li class="service-item"><svg class="tick" viewBox="0 0 24 24"><circle cx="12" cy="12" r="12" fill="var(--green)"/><path d="M7 12.5l3.2 3.2L17 9" fill="none" stroke="var(--white)" stroke-width="2.6" stroke-linecap="round" stroke-linejoin="round"/></svg>Utilization Management</li>
      <li class="service-item"><svg class="tick" viewBox="0 0 24 24"><circle cx="12" cy="12" r="12" fill="var(--green)"/><path d="M7 12.5l3.2 3.2L17 9" fill="none" stroke="var(--white)" stroke-width="2.6" stroke-linecap="round" stroke-linejoin="round"/></svg>Clinical Documentation Integrity</li>
      <li class="service-item"><svg class="tick" viewBox="0 0 24 24"><circle cx="12" cy="12" r="12" fill="var(--green)"/><path d="M7 12.5l3.2 3.2L17 9" fill="none" stroke="var(--white)" stroke-width="2.6" stroke-linecap="round" stroke-linejoin="round"/></svg>Peer to Peer Appeals</li>
      <li class="service-item"><svg class="tick" viewBox="0 0 24 24"><circle cx="12" cy="12" r="12" fill="var(--green)"/><path d="M7 12.5l3.2 3.2L17 9" fill="none" stroke="var(--white)" stroke-width="2.6" stroke-linecap="round" stroke-linejoin="round"/></svg>Letter Appeal Management</li>
    </ul>
  </section>

  <svg class="desk-photo" width="318" height="222" viewBox="0 0 318 222">
    <defs>
      <linearGradient id="deskTone" x1="0" y1="0" x2="1" y2="1">
        <stop offset="0" stop-color="var(--desk-dark)"/>
        <stop offset="0.5" stop-color="var(--desk-light)"/>
        <stop offset="1" stop-color="#c9cfc4"/>
      </linearGradient>
    </defs>
    <path fill="url(#deskTone)" role="img" aria-label="Photo: laptop, calculator, financial reports and stacks of dollar bills on a desk" d="M0 0 H318 V172 L0 221 Z"/>
  </svg>
</main>
</body>
</html>
```